KESTRIL sales brochure

Our company, MeadowLanternly, has recently undertaken a re-branding overhaul to change our website and corporate materials (color scheme, letterhead, biz cards). In support of this re-branding effort, we need an initial sales brochure designed for our company's services that will reflect the look and feel of the website. The website design, fonts and images are included as attachments for your reference.

The brochure will be distributed primarily via email. The audience will be prospective buyers - generally pharmaceutical companies or smaller biotech companies, either of whom are developing treatments for different diseases.

Attached is a word document which contains the text for the brochure. The powerpoint document titled 'case studies' provides example charts and graphs that can be used.
We would like a final format in a layered PSD (photoshop file).

A modular brochure that would allow us to include one or more case studies based on the sales opportunity would be a plus.
Updates

Attention: The text for the brochure has been updated.

Target Market(s)

Pharmaceutical companies / biotechnology companies

Industry/Entity Type

Pharmaceutical

Requirements
Must have
• Utilize the images we have provided as attachments where possible. And choose from our color palette and fonts.
Nice to have
• Additional graphics that reflect the look and feel per our attachments.

```html
<!DOCTYPE html>
<html lang="en">
<head>
<meta charset="utf-8">
<title>MeadowLanternly — Case Studies</title>
<link href="https://fonts.googleapis.com/css2?family=Nunito+Sans:ital,wght@0,400;0,600;0,700;0,800;1,400;1,600&display=swap" rel="stylesheet">
<style>
  :root {
    --stage: #000000;
    --paper: #ffffff;
    --band: #58585a;
    --cyan: #1ea7d8;
    --cyan-light: #8fd3ef;
    --orange: #f7a823;
    --yellow: #fde38a;
    --olive: #6b8a3f;
    --ink: #3d3d3f;
    --ink-soft: #58585a;
    --grid: #e2e2e2;
    --grey-bar: #cfcfcf;
    --dark-bar: #4a4a4c;
  }
  * { margin: 0; padding: 0; box-sizing: border-box; }
  html, body { width: 1200px; height: 814px; overflow: hidden; background: var(--stage); }
  body { font-family: "Nunito Sans", Arial, sans-serif; color: var(--ink); position: relative; }

  .slide { position: absolute; width: 571px; height: 378px; background: var(--paper); overflow: hidden; }
  .slide--dystrophy { left: 20px; top: 20px; }
  .slide--connections { left: 608px; top: 20px; }
  .slide--survival { left: 20px; top: 415px; }
  .slide--lipodystrophy { left: 608px; top: 418px; height: 376px; }

  .slide__kicker { position: absolute; left: 44px; top: 30px; font-size: 29px; font-weight: 800; color: var(--cyan); letter-spacing: 0.5px; }
  .slide__band { position: absolute; left: 0; right: 0; bottom: 0; height: 66px; background: var(--band); }
  .slide__brand { position: absolute; right: 34px; bottom: 18px; font-size: 17px; font-weight: 400; color: var(--paper); letter-spacing: 0.3px; }

  .study-title { position: absolute; font-size: 15px; font-weight: 700; line-height: 1.12; color: var(--ink); }
  .challenge { position: absolute; font-size: 11.5px; line-height: 1.42; }
  .challenge__label { font-weight: 700; font-style: normal; display: block; }
  .challenge__text { font-style: italic; }

  .chart { position: absolute; overflow: visible; font-family: "Nunito Sans", Arial, sans-serif; }

  .slide--dystrophy .study-title { left: 78px; top: 102px; width: 130px; }
  .slide--dystrophy .challenge { left: 78px; top: 148px; width: 128px; }

  .slide--connections .study-title { left: 44px; top: 72px; }
  .connections__headline { position: absolute; left: 0; right: 0; top: 196px; text-align: center; font-size: 15.5px; font-weight: 800; line-height: 1.05; color: var(--orange); }
  .connections__body { position: absolute; left: 100px; width: 371px; top: 238px; text-align: center; font-size: 12px; line-height: 1.32; color: var(--ink-soft); }

  .slide--survival .study-title { left: 44px; top: 84px; }
  .slide--survival .challenge { left: 44px; top: 110px; width: 108px; }

  .slide--lipodystrophy .study-title { left: 44px; top: 70px; width: 140px; }
  .slide--lipodystrophy .challenge { left: 44px; top: 128px; width: 148px; font-size: 10.5px; line-height: 1.36; color: var(--ink-soft); }
  .slide--lipodystrophy .challenge__label { color: var(--ink); }
</style>
</head>
<body>

<section class="slide slide--dystrophy">
  <h2 class="slide__kicker">CASE STUDY</h2>
  <h3 class="study-title">Decoding Muscular Dystrophy</h3>
  <p class="challenge"><span class="challenge__label">Challenge:</span><span class="challenge__text">As research activity on Duchenne-Becker muscular dystrophy surged in the last decade, investigators needed a platform to communicate with a global patient base.</span></p>

  <svg class="chart" style="left:232px;top:96px" width="290" height="210" viewBox="0 0 290 210" aria-label="Line chart of patients and trials, 2007 to 2013">
    <g stroke="var(--grid)" stroke-width="0.8">
      <line x1="50" y1="10" x2="226" y2="10"/><line x1="50" y1="27.5" x2="226" y2="27.5"/>
      <line x1="50" y1="45" x2="226" y2="45"/><line x1="50" y1="62.5" x2="226" y2="62.5"/>
      <line x1="50" y1="80" x2="226" y2="80"/><line x1="50" y1="97.5" x2="226" y2="97.5"/>
      <line x1="50" y1="115" x2="226" y2="115"/><line x1="50" y1="132.5" x2="226" y2="132.5"/>
    </g>
    <line x1="50" y1="150" x2="226" y2="150" stroke="#9a9a9a" stroke-width="0.8"/>
    <g font-size="8" fill="var(--ink)" text-anchor="end">
      <text x="44" y="13">4000</text><text x="44" y="30.5">3500</text><text x="44" y="48">3000</text>
      <text x="44" y="65.5">2500</text><text x="44" y="83">2000</text><text x="44" y="100.5">1500</text>
      <text x="44" y="118">1000</text><text x="44" y="135.5">500</text><text x="44" y="153">0</text>
    </g>
    <g font-size="8" fill="var(--ink)" text-anchor="start">
      <text x="232" y="13">40</text><text x="232" y="30.5">35</text><text x="232" y="48">30</text>
      <text x="232" y="65.5">25</text><text x="232" y="83">20</text><text x="232" y="100.5">15</text>
      <text x="232" y="118">10</text><text x="232" y="135.5">5</text><text x="232" y="153">0</text>
    </g>
    <g font-size="6.5" font-weight="700" fill="var(--ink)" text-anchor="middle">
      <text x="62" y="164">2007</text><text x="87" y="164">2008</text><text x="112" y="164">2009</text>
      <text x="138" y="164">2010</text><text x="163" y="164">2011</text><text x="188" y="164">2012</text><text x="214" y="164">2013</text>
    </g>
    <text transform="translate(12 150) rotate(-90)" font-size="6" fill="var(--ink)"># patients needed for studies vs patients in registry</text>
    <text transform="translate(250 145) rotate(-90)" font-size="6" fill="var(--ink)"># of trials (source - trialledger.org)</text>

    <polyline fill="none" stroke="var(--cyan-light)" stroke-width="1.6" points="62,146.5 87,134.3 112,130.8 138,113.3 163,125.5 188,118.5 214,99.3"/>
    <g fill="var(--cyan-light)"><circle cx="62" cy="146.5" r="2"/><circle cx="87" cy="134.3" r="2"/><circle cx="112" cy="130.8" r="2"/><circle cx="138" cy="113.3" r="2"/><circle cx="163" cy="125.5" r="2"/><circle cx="188" cy="118.5" r="2"/><circle cx="214" cy="99.3" r="2"/></g>

    <polyline fill="none" stroke="var(--yellow)" stroke-width="1.8" points="62,130.8 87,111.5 112,87 138,74.8 163,55.5 188,41.5 214,25.8"/>
    <g fill="var(--yellow)"><circle cx="62" cy="130.8" r="2"/><circle cx="87" cy="111.5" r="2"/><circle cx="112" cy="87" r="2"/><circle cx="138" cy="74.8" r="2"/><circle cx="163" cy="55.5" r="2"/><circle cx="188" cy="41.5" r="2"/><circle cx="214" cy="25.8" r="2"/></g>

    <polyline fill="none" stroke="var(--orange)" stroke-width="1.8" points="62,125.5 87,111.5 112,104.5 138,55.5 163,41.5 188,66 214,24"/>
    <g fill="var(--orange)"><circle cx="62" cy="125.5" r="2"/><circle cx="87" cy="111.5" r="2"/><circle cx="112" cy="104.5" r="2"/><circle cx="138" cy="55.5" r="2"/><circle cx="163" cy="41.5" r="2"/><circle cx="188" cy="66" r="2"/><circle cx="214" cy="24" r="2"/></g>

    <g font-size="6" fill="var(--ink)">
      <line x1="30" y1="177" x2="46" y2="177" stroke="var(--cyan-light)" stroke-width="1.6"/><circle cx="38" cy="177" r="2" fill="var(--cyan-light)"/>
      <text x="38" y="188" text-anchor="middle"># of patients needed for trials</text>
      <line x1="120" y1="177" x2="136" y2="177" stroke="var(--yellow)" stroke-width="1.6"/><circle cx="128" cy="177" r="2" fill="var(--yellow)"/>
      <text x="128" y="188" text-anchor="middle"># patients in registry</text>
      <line x1="198" y1="177" x2="214" y2="177" stroke="var(--orange)" stroke-width="1.6"/><circle cx="206" cy="177" r="2" fill="var(--orange)"/>
      <text x="206" y="188" text-anchor="middle"># of trials</text>
    </g>
  </svg>

  <div class="slide__band"><span class="slide__brand">MeadowLanternly</span></div>
</section>

<section class="slide slide--connections">
  <h2 class="slide__kicker">CASE STUDY</h2>
  <h3 class="study-title">Creating Connections</h3>

  <svg class="chart" style="left:140px;top:94px" width="290" height="100" viewBox="0 0 290 100" aria-label="Overlap of Down syndrome and Alzheimer's, 40 percent">
    <defs><clipPath id="overlap-clip"><circle cx="118" cy="50" r="41"/></clipPath></defs>
    <circle cx="118" cy="50" r="41" fill="var(--cyan)"/>
    <circle cx="166" cy="50" r="43" fill="var(--orange)"/>
    <circle cx="166" cy="50" r="43" fill="var(--olive)" clip-path="url(#overlap-clip)"/>
    <polyline fill="none" stroke="#2f4a5a" stroke-width="1" points="80,58 95,50 105,56 113,42 124,56 134,47"/>
    <text x="142" y="54" text-anchor="middle" font-size="11" font-weight="800" fill="var(--paper)">40%</text>
    <g font-size="6" font-weight="600" fill="var(--ink)" text-anchor="end">
      <text x="70" y="48">DOWN</text><text x="70" y="56">SYNDROME</text>
    </g>
    <text x="222" y="52" font-size="6" font-weight="600" fill="var(--ink)">ALZHEIMER</text>
  </svg>

  <p class="connections__headline">WHAT CAN DOWN SYNDROME<br>TELL US ABOUT ALZHEIMER’S?</p>
  <p class="connections__body">By age 40, a full 40 percent of people with Down Syndrome will also develop Alzheimer’s. We’re helping researchers understand why. Because we collect consistent pan-disease data, we’ve created new opportunities to study how conditions interact.</p>

  <div class="slide__band"><span class="slide__brand">MeadowLanternly</span></div>
</section>

<section class="slide slide--survival">
  <h2 class="slide__kicker">CASE STUDY</h2>
  <h3 class="study-title">Survival Story</h3>
  <p class="challenge"><span class="challenge__label">Challenge:</span><span class="challenge__text">Harbor Wellness Circle, a global nonprofit, needed insight into the breast cancer experience to help more patients navigate each stage of their journey with the illness</span></p>

  <svg class="chart" style="left:150px;top:140px" width="400" height="150" viewBox="0 0 400 150" aria-label="Bar chart of cancer survivors in registry">
    <rect x="78" y="20" width="2.3" height="20" fill="var(--cyan)"/>
    <rect x="78" y="51" width="149" height="27" fill="var(--yellow)"/>
    <rect x="78" y="87" width="287" height="27" fill="var(--orange)"/>
    <line x1="78" y1="10" x2="78" y2="118" stroke="#9a9a9a" stroke-width="0.8"/>
    <g font-size="8.5" font-weight="600" fill="var(--ink)" text-anchor="middle">
      <text x="48" y="28">Cancer</text><text x="48" y="37">areas</text>
      <text x="40" y="62">Breast cancer</text><text x="48" y="71">survivors</text>
      <text x="40" y="98">All cancer</text><text x="48" y="107">survivors</text>
    </g>
    <g font-size="9" fill="var(--ink)">
      <text x="86" y="33">40</text><text x="233" y="68">2,600</text><text x="371" y="104">5,000</text>
    </g>
    <g font-size="9" fill="var(--ink)" text-anchor="middle">
      <text x="78" y="135">0</text><text x="135" y="135">1000</text><text x="193" y="135">2000</text>
      <text x="250" y="135">3000</text><text x="308" y="135">4000</text><text x="365" y="135">5000</text>
    </g>
  </svg>

  <div class="slide__band"><span class="slide__brand">MeadowLanternly</span></div>
</section>

<section class="slide slide--lipodystrophy">
  <h2 class="slide__kicker">CASE STUDY</h2>
  <h3 class="study-title">Leading the Way: Collaboration in Lipodystrophy</h3>
  <p class="challenge"><span class="challenge__label">Challenge:</span><span class="challenge__text">Two major pharmaceutical companies working together to develop a treatment for lipodystrophy need a population’s worth of data. The only trouble is there’s almost no clinical information about the condition, no one knows how many people are affected or where they live.</span></p>

  <svg class="chart" style="left:160px;top:80px" width="400" height="200" viewBox="0 0 400 200" aria-label="Bar chart of patients in registry by country">
    <rect x="118" y="12" width="8" height="17" fill="var(--dark-bar)"/>
    <rect x="118" y="39" width="8" height="17" fill="var(--grey-bar)"/>
    <rect x="118" y="67" width="8" height="17" fill="var(--cyan)"/>
    <rect x="118" y="95" width="24" height="17" fill="var(--cyan-light)"/>
    <rect x="118" y="121" width="122" height="17" fill="var(--yellow)"/>
    <rect x="118" y="149" width="236" height="17" fill="var(--orange)"/>
    <line x1="118" y1="6" x2="118" y2="170" stroke="#9a9a9a" stroke-width="0.8"/>
    <g font-size="8.5" font-weight="600" fill="var(--ink)" text-anchor="end">
      <text x="110" y="24">Venezuela</text><text x="110" y="51">United Kingdom</text>
      <text x="110" y="79">Pakistan</text><text x="110" y="107">Canada</text>
      <text x="110" y="133">Spain</text><text x="110" y="161">United States</text>
    </g>
    <g font-size="9" fill="var(--ink)">
      <text x="132" y="24">1</text><text x="132" y="51">1</text><text x="132" y="79">1</text>
      <text x="148" y="107">3</text><text x="246" y="133">15</text><text x="360" y="161">29</text>
    </g>
    <g font-size="9" fill="var(--ink)" text-anchor="middle">
      <text x="118" y="184">0</text><text x="159" y="184">5</text><text x="199" y="184">10</text>
      <text x="240" y="184">15</text><text x="281" y="184">20</text><text x="321" y="184">25</text><text x="362" y="184">30</text>
    </g>
    <text x="118" y="197" font-size="6" fill="var(--ink)">Number of patients in registry during first month of operation</text>
  </svg>

  <div class="slide__band"><span class="slide__brand">MeadowLanternly</span></div>
</section>

</body>
</html>
```